Redesign of Bright Harbor Entertainment Card

I already have my logo and font design for my company name. I am looking to come up with a Unique way of having it on my business card. Just looking for a really hip, and professional business card while still using my logo design.

I have also enclosed the front and back of the card so you can see what I have now. Looking for something different.

Thank you!

Target Market(s)

Young to middle aged brides and grooms

Industry/Entity Type

Business

Requirements
Should not have
• Cheese

```html
<!DOCTYPE html>
<html lang="en">
<head>
<meta charset="UTF-8">
<title>Bright Harbor Entertainment – Business Card</title>
<link rel="stylesheet" href="https://fonts.googleapis.com/css2?family=Oswald:wght@300;400&family=Open+Sans:wght@400&display=swap">
<style>
  :root {
    --card-bg: #ffffff;
    --ink-navy: #1a3a9f;
    --ink-sky: #35b5e4;
    --mark-faint: #efefef;
  }
  html, body {
    margin: 0;
    padding: 0;
    width: 1200px;
    height: 695px;
    overflow: hidden;
    background: var(--card-bg);
  }
  .card {
    position: relative;
    width: 1200px;
    height: 695px;
    background: var(--card-bg);
    overflow: hidden;
  }
  .brand-ring {
    position: absolute;
    left: 0;
    top: 0;
    width: 1200px;
    height: 695px;
  }
  .brand-watermark {
    position: absolute;
    left: 0;
    right: 0;
    top: 120px;
    text-align: center;
    font-family: 'Oswald', sans-serif;
    font-weight: 400;
    font-size: 64px;
    line-height: 1;
    letter-spacing: 2px;
    text-transform: uppercase;
    color: var(--mark-faint);
    white-space: nowrap;
  }
  .identity {
    position: absolute;
    left: 0;
    right: 0;
    top: 248px;
    text-align: center;
    font-family: 'Oswald', sans-serif;
    font-weight: 300;
    font-size: 70px;
    line-height: 78px;
    color: var(--ink-navy);
  }
  .identity p { margin: 0; }
  .contact {
    position: absolute;
    left: 0;
    right: 0;
    top: 514px;
    text-align: center;
    font-family: 'Open Sans', sans-serif;
    font-weight: 400;
    font-size: 35px;
    line-height: 44px;
    color: var(--ink-sky);
  }
  .contact p { margin: 0; }
</style>
</head>
<body>
  <main class="card">
    <svg class="brand-ring" viewBox="0 0 1200 695" aria-hidden="true">
      <circle cx="600" cy="346" r="304" fill="none" stroke="var(--mark-faint)" stroke-width="16"/>
    </svg>
    <div class="brand-watermark" aria-hidden="true">Bright Harbor</div>

    <section class="identity">
      <p class="dj-name">DJ Sam Rivera</p>
      <p class="email">info@brightharbor.com</p>
    </section>

    <section class="contact">
      <p class="phone">555 - 014 - 2837</p>
      <p class="website">brightharbor.com</p>
      <p class="social">harborlink.net/brightharborevents</p>
    </section>
  </main>
</body>
</html>
```